Graphic Design: html email newsletter/Mail Chimp

We need a sophisticated html graphic design for an email newsletter template, that we'd be likely posting via mail chimp.
We are an engineering consultancy so the design needs to be very professional...but visually pleasing and graphically sophisticated with 'depth'/ 'layering' - and not boring.
Current branding information available, as well as rough prelim, and an example that we like.

Target Market(s)

Architects, town planners, developers

Industry/Entity Type

Graphic Design

Number of Pages Required

1 page

Colors
33a6d7
85cae6

Requirements
Must have
• The newsletter will require:
• - a title section
• - intro text section
• - 6 internal news articles with images (i.e. work that we are doing)
• - 1 or 2 external news articles with images (i.e.. stuff we like external to our business)
• - possibly a map of project locations that would change month to month
• Check out:
• 1. our website fernmarsh.net for colours and branding
• 2. an example of what we like: http://ex4.newsletter-vault7.com/?u=91fa3b2d07c4e5816a2f9d357&id=d4f0a81b6e&e=7c2e9f41ab
• 3. a scrappy concept that needs significant design input/flair: https://ex8.admin.postlarkly.com/templates/edit?id=73052
• Logo, business card and company profile files attached. The blues in the company profile are more preferred over the basic cyan of the business cards.

```html
<!DOCTYPE html>
<html lang="en">
<head>
<meta charset="utf-8">
<title>Fernmarsh Collective Newsletter</title>
<link href="https://fonts.googleapis.com/css2?family=Alegreya:wght@400;700&family=Alegreya+Sans:wght@400;700&family=Questrial&display=swap" rel="stylesheet">
<style>
:root{
  --blue:#33a6d7;
  --blue-soft:#85cae6;
  --ink:#222222;
  --text:#333333;
  --rule:#c9c9c9;
  --topbar:#111111;
  --footer:#2f2f2f;
  --white:#ffffff;
  --muted:#9a9a9a;
}
*{margin:0;padding:0;box-sizing:border-box}
html,body{width:1200px;height:3338px;overflow:hidden;background:var(--white)}
body{position:relative;font-family:"Alegreya",Georgia,serif;color:var(--text)}
.abs{position:absolute}
.topbar{left:0;top:0;width:1200px;height:40px;background:var(--topbar);color:var(--white);
  font-family:"Alegreya Sans",Arial,sans-serif;font-size:20px;line-height:40px;text-align:center}
.topbar b{font-weight:700}
.header-band{left:0;top:40px;width:1200px;height:648px;background:var(--blue)}
.tagline{left:0;width:1200px;text-align:center;color:var(--white);font-family:"Questrial",Arial,sans-serif;font-size:28px;line-height:1}
.brand{left:0;top:100px;width:1200px;text-align:center;color:var(--ink);font-family:"Questrial",Arial,sans-serif;font-size:58px;line-height:1}
.hero{left:135px;top:215px;width:922px;height:649px;border:3px solid var(--white);border-radius:18px;overflow:hidden;
  background:linear-gradient(180deg,#cfd6dc 0%,#e9e4dc 30%,#b89a74 62%,#7a4a26 100%)}
.hero-caption{left:426px;top:664px;width:617px;height:182px;background:var(--blue);color:var(--white);padding:12px 18px}
.hero-caption h2{font-size:30px;font-weight:700;line-height:1.1;margin-bottom:8px}
.hero-caption p{font-size:20.5px;line-height:25px}
.contents-side{top:920px;height:150px;background:var(--blue)}
.contents-title{left:0;top:891px;width:1200px;text-align:center;font-size:31px;font-weight:700;color:var(--ink)}
.contents-list{list-style:none;font-family:"Questrial",Arial,sans-serif;font-size:26px;color:var(--ink);line-height:38.5px}
.contents-list li::before{content:">";color:var(--blue);font-weight:700;margin-right:12px}
.h-title{left:0;top:1092px;width:1200px;text-align:center;font-size:62px;font-weight:700;color:var(--ink)}
.copy{font-size:22.5px;line-height:29px;color:var(--text)}
.small-copy{font-size:20.5px;line-height:25px;color:var(--text)}
.btn{height:52px;background:var(--blue);color:var(--white);font-family:"Alegreya Sans",Arial,sans-serif;font-size:25px;
  line-height:52px;text-align:center;box-shadow:0 6px 6px rgba(0,0,0,.28)}
.rule{left:135px;width:922px;height:3px;background:var(--rule)}
.h-two{left:0;top:1475px;width:1200px;text-align:center;font-size:44px;font-weight:700;color:var(--ink)}
.h-four,.h-three{font-size:40px;font-weight:700;color:var(--ink);line-height:1}
.thumb{top:1624px;width:224px;height:139px}
.footer{left:0;top:2759px;width:1200px;height:579px;background:var(--footer);color:var(--white)}
.footer h3{font-family:"Alegreya Sans",Arial,sans-serif;font-size:37px;font-weight:700;color:var(--white)}
.office{font-family:"Alegreya Sans",Arial,sans-serif;font-size:20px;line-height:29px;color:var(--white)}
.office h4{font-size:25px;font-weight:700;margin-bottom:2px}
.office .gap{height:14px}
.social{display:flex;align-items:center;font-family:"Alegreya Sans",Arial,sans-serif;font-size:17px;color:#bbbbbb}
.social .ring{width:36px;height:36px;border:2px solid #cfcfcf;border-radius:50%;margin-right:8px;display:flex;align-items:center;justify-content:center}
.legal{left:0;width:1200px;text-align:center;font-family:Arial,Helvetica,sans-serif;color:var(--white)}
.legal a{color:var(--muted)}
</style>
</head>
<body>

<div class="abs topbar">We've got some news for you | <b>Web Version</b></div>

<div class="abs header-band"></div>
<div class="abs tagline" style="top:62px">structural design studio</div>
<div class="abs brand">Fernmarsh Collective</div>
<div class="abs tagline" style="top:170px">considered engineering</div>

<div class="abs hero" role="img" aria-label="Photograph of a bright open-plan living room with timber floors, sliding glass doors and clerestory louvres"></div>
<div class="abs hero-caption">
  <h2>Ashcombe Road Alterations and Additions</h2>
  <p>The framing of different roof levels enable the incorporation of clearstory louvers to the new living room, and a combination of bracing and sway-frames were incorporated at the outer edge of the external room.</p>
</div>

<div class="abs contents-side" style="left:0;width:218px"></div>
<div class="abs contents-side" style="left:969px;width:231px"></div>
<div class="abs contents-title">Newsletter Contents</div>
<ul class="abs contents-list" style="left:276px;top:947px">
  <li>Item Number One</li><li>Item Number Two</li><li>Item Number Three</li>
</ul>
<ul class="abs contents-list" style="left:675px;top:947px">
  <li>Item Number Four</li><li>Item Number Five</li><li>Item Number Six</li>
</ul>

<h1 class="abs h-title">Title Section</h1>
<p class="abs copy" style="left:135px;top:1188px;width:922px">Intro text here. Sit amet, consectetur adipiscing elit. Donec congue tortor a males vitae uada condimentum. Duis dictum nunc dolor. Maecenas sed mollis tortor id del a porta. Vivamus scelerisque diam sapien, quis faucibus velit tempor venenatis.</p>
<p class="abs copy" style="left:135px;top:1305px;width:922px">Maecenas et risus et nulla finibus dictum. Cras sagittis felis sit amet mollis interdum. Cras ornare dapibus sapien, eget feugiat ipsum sodales quis. Nulla facilisi. Phasellus hendrerit orci sed augue sagittis ultrices.</p>
<div class="abs btn" style="left:825px;top:1395px;width:232px">READ MORE</div>

<div class="abs rule" style="top:1469px"></div>
<h2 class="abs h-two">Heading Two...</h2>
<div class="abs rule" style="top:1541px"></div>

<h3 class="abs h-four" style="left:135px;top:1568px">Heading Four</h3>
<div class="abs thumb" style="left:135px;background:linear-gradient(180deg,#9fb3c4,#c9c3b6 55%,#6d6a63)" role="img" aria-label="Photograph of a residential tower at street level"></div>
<div class="abs thumb" style="left:368px;background:linear-gradient(180deg,#7ea4d4,#d9dde0 50%,#8d8a83)" role="img" aria-label="Photograph of a mixed-use building with a tower behind"></div>
<div class="abs thumb" style="left:601px;background:linear-gradient(180deg,#b9cde0,#e4e4e0 55%,#7f7f7a)" role="img" aria-label="Photograph of a low civic building with a flagpole"></div>
<div class="abs thumb" style="left:834px;background:linear-gradient(180deg,#3c4450,#5b88b8 45%,#2e2d2b)" role="img" aria-label="Photograph of a car park entry with level signage"></div>
<p class="abs small-copy" style="left:135px;top:1785px;width:922px">Donec pharetra quam et metus laoreet rhoncus. Aene ngue congue lacus. In euismod malesuada el. Quis consectetur dolor. Sapien mauris, rhoncus a lacus nec congue congue lacus. In euismod el ala malesuada est, quis consectetur doloru est.</p>

<div class="abs rule" style="top:1879px"></div>

<div class="abs" style="left:135px;top:1911px;width:370px;height:377px;background:linear-gradient(160deg,#5d7fa6 0%,#8aa0b0 40%,#c59a52 65%,#4c4237 100%)" role="img" aria-label="Photograph of an angular pavilion canopy lit from below at dusk"></div>
<h3 class="abs h-three" style="left:536px;top:1911px">Heading Three One</h3>
<p class="abs small-copy" style="left:536px;top:1963px;width:521px">Donec pharetra quam et metus laoreet rhoncus. Aene sapien mauris, rhoncus a lacus nec, congue congue lacus. In euismod malesuada est, quis consectetur dolor semper nec. In molestie ante at lacus elementum maximus sapien mauris, rhoncus a lacus nec, congue congue lacus. In euismod malesuada est, quis consectetur dolor. Sapien mauris, rhoncus a lacus nec, congue congue lacus. In euismod malesuada est, quis consectetur doloru est.</p>
<div class="abs btn" style="left:534px;top:2230px;width:229px">READ MORE</div>
<div class="abs btn" style="left:825px;top:2230px;width:232px">CONTACT US</div>

<div class="abs rule" style="top:2318px"></div>

<h3 class="abs h-three" style="left:137px;top:2346px">Heading Three Two</h3>
<p class="abs small-copy" style="left:137px;top:2402px;width:525px">Donec pharetra quam et metus laoreet rhoncus. Aene sapien mauris, rhoncus a lacus nec, congue congue lacus. In euismod malesuada est, quis consectetur dolor semper nec. In molestie ante at lacus elementum maximus sapien mauris, rhoncus a lacus nec, congue congue lacus. In euismod malesuada est, quis consectetur dolor. Sapien mauris, rhoncus a lacus nec, congue congue lacus. In euismod malesuada est, quis consectetur doloru est.</p>
<div class="abs btn" style="left:137px;top:2676px;width:233px">READ MORE</div>
<div class="abs btn" style="left:426px;top:2676px;width:231px">CONTACT US</div>
<div class="abs" style="left:686px;top:2351px;width:375px;height:381px;background:linear-gradient(170deg,#5e86b4 0%,#c9c6b8 45%,#8a7c66 75%,#4a4740 100%)" role="img" aria-label="Photograph of an apartment building with stacked balconies"></div>

<div class="abs footer">
  <h3 class="abs" style="left:141px;top:26px">Our Offices:</h3>
  <div class="abs" style="left:135px;top:79px;width:922px;height:3px;background:var(--white)"></div>

  <div class="abs office" style="left:141px;top:110px">
    <h4>Sydney Office</h4>
    Loftline Studio<br>42 Tallow Bank Road<br>Wrenfield, NSW 2094
    <div class="gap"></div>
    +61 (0)2 9000 4172<br>sydney@fernmarsh.net
  </div>
  <div class="abs office" style="left:487px;top:110px">
    <h4>Brisbane Office</h4>
    17 Cadell Lane<br>Marrow Heights, QLD 4019
    <div class="gap"></div>
    +61 (0)7 3000 2864<br>brisbane@fernmarsh.net
  </div>
  <div class="abs office" style="left:857px;top:110px">
    <h4>Pacific Alliance</h4>
    S8 Coral Row<br>Kelvale NCD<br>Papua New Guinea
    <div class="gap"></div>
    +675 700 04219<br>pom@fernmarsh.net
  </div>

  <div class="abs social" style="left:240px;top:354px"><span class="ring"></span>Linkfold</div>
  <div class="abs social" style="left:400px;top:354px"><span class="ring"></span>Chirpline</div>
  <div class="abs social" style="left:536px;top:354px"><span class="ring"></span>Circlespace</div>
  <div class="abs social" style="left:713px;top:354px"><span class="ring">
    <svg width="18" height="18" viewBox="0 0 18 18" fill="none" stroke="#cfcfcf" stroke-width="2"><path d="M7 11l4-4M6 8L4 10a2.8 2.8 0 004 4l2-2M12 10l2-2a2.8 2.8 0 00-4-4L8 6"/></svg>
  </span>FMC.com</div>
  <div class="abs social" style="left:872px;top:354px"><span class="ring">
    <svg width="18" height="14" viewBox="0 0 18 14" fill="none" stroke="#cfcfcf" stroke-width="2"><rect x="1" y="1" width="16" height="12"/><path d="M1 1l8 7 8-7"/></svg>
  </span>Email</div>

  <div class="abs legal" style="top:434px;font-size:16px">Copyright © Fernmarsh Design Studio 2015, Al rights reserved.</div>
  <div class="abs legal" style="top:472px;font-size:16px">Our mailing adress is:</div>
  <div class="abs legal" style="top:495px;font-size:22px;font-weight:700">info@fernmarsh.com</div>
  <div class="abs legal" style="top:536px;font-size:15px"><a>unsubscribe from this list</a> &nbsp;&nbsp; <a>update subscription preferences</a></div>
</div>

</body>
</html>
```